Hello Team Telvu,

So the "KR" logo you have designed we need to continue the same continuity carried out onto the label design. clean, not busy, eye catchy, up market, high end label, house hold consumer.

I will upload a few images of something similar to what we are after.

- Able to see most of the product without the label covering it.

- Label background will be clear, so that product is still visible. this point in time the packaging that will be used is not large, I will send you tub dimension and image.

- There will be 4 x flavours at this stage we don't know the flavours yet, I will confirm in the next few weeks which flavours we will be producing.

- Let's start the design now at least so that I can get a feel of what we will be happy with.

- I will also attach a photo of one of the products we will be making which will be part of the 4x flavours, so that you can have an idea of designs and where we are headed.

- As you can see regarding the attached pictures, the 3x containers stacked on top of each other is the product we will be manufacturing in the exact same tub.

I am not sure of the flavours as yet, which knowing what 4 x flavours we are running with will take another month to decide. i want to get the layout of the labels done firstly. once i'm happy with the layout and i know the flavours we can proceed to finalise artwork. that may take approximately 1 month.

```html
<!DOCTYPE html>
<html lang="en">
<head>
<meta charset="utf-8">
<title>Kestrel Ridge – Shanklish Tub Labels</title>
<link href="https://fonts.googleapis.com/css2?family=Montserrat:wght@500&family=Lato:wght@300;400&family=Arimo:wght@400;700&display=swap" rel="stylesheet">
<style>
  :root {
    --ink: #050505;
    --paper: #ffffff;
    --gold: #d9ad45;
    --gold-deep: #b08a35;
    --die: #d8262c;
  }
  html, body {
    margin: 0;
    width: 1200px;
    height: 1200px;
    overflow: hidden;
    background: var(--paper);
  }
  .artboard {
    position: relative;
    width: 1500px;
    height: 1500px;
    transform: scale(0.8);
    transform-origin: 0 0;
  }
  .sheet {
    position: absolute;
    left: 0;
    top: 180px;
    width: 1500px;
    height: 1100px;
  }
  .shapes { position: absolute; left: 0; top: 0; }

  .brand-dot {
    position: absolute;
    border-radius: 50%;
    background: var(--gold);
  }
  .brand-name {
    position: absolute;
    text-align: center;
    font-family: "Montserrat", sans-serif;
    font-weight: 500;
    line-height: 1;
    color: var(--paper);
    letter-spacing: 0.08em;
    white-space: nowrap;
  }

  /* lid label */
  .lid-dot { left: 727px; top: 274px; width: 46px; height: 46px; }
  .lid-name { left: 550px; top: 346px; width: 400px; font-size: 27px; }
  .olive-sprig {
    position: absolute;
    left: 724px; top: 422px; width: 44px; height: 46px;
    border-radius: 50%;
    background: radial-gradient(circle at 50% 55%, #ffffff 0 40%, #cfcfcf 70%, transparent 71%);
  }
  .lid-tagline {
    position: absolute;
    left: 648px; top: 473px; width: 200px;
    text-align: center;
    font-family: "Arimo", sans-serif;
    font-weight: 700; font-style: italic;
    font-size: 10px; color: var(--paper);
  }

  /* front panel of wrap */
  .front-dot { left: 760px; top: 728px; width: 30px; height: 30px; }
  .front-name { left: 677px; top: 776px; width: 200px; font-size: 16px; }
  .product-name {
    position: absolute;
    left: 627px; top: 832px; width: 300px;
    text-align: center;
    font-family: "Lato", sans-serif; font-weight: 300;
    font-size: 39px; line-height: 1; color: var(--gold);
    letter-spacing: 0.01em;
  }
  .product-sub {
    position: absolute;
    left: 627px; top: 866px; width: 300px;
    text-align: center;
    font-family: "Lato", sans-serif; font-weight: 400;
    font-size: 21px; line-height: 1.1; color: var(--paper);
  }
  .net-weight {
    position: absolute;
    left: 742px; top: 927px; width: 70px;
    text-align: center;
    font-family: "Arimo", sans-serif; font-weight: 700;
    font-size: 15px; color: var(--paper);
  }

  /* side panels */
  .side-panel {
    position: absolute;
    top: 713px;
    width: 194px; height: 310px;
    background: var(--ink);
    color: var(--paper);
    font-family: "Arimo", sans-serif;
    box-sizing: border-box;
  }
  .side-panel--nutrition {
    left: 187px;
    transform: rotate(-10deg);
    padding: 36px 10px 0 14px;
  }
  .side-panel--info {
    left: 1169px;
    transform: rotate(10deg);
    padding: 78px 14px 0 14px;
  }
  .nutrition-box {
    border: 1px solid var(--paper);
    padding: 4px 5px 3px;
  }
  .nutrition-title { font-weight: 700; font-size: 17px; line-height: 1; }
  .nutrition-meta { font-size: 8.5px; line-height: 1.2; border-bottom: 4px solid var(--paper); padding-bottom: 3px; }
  .nutrition-table { width: 100%; border-collapse: collapse; font-size: 8.5px; }
  .nutrition-table th, .nutrition-table td { border-top: 1px solid var(--paper); padding: 1px 2px; font-weight: 400; text-align: left; }
  .nutrition-table td + td, .nutrition-table th + th { border-left: 1px solid var(--paper); text-align: center; }
  .nutrition-origin { font-size: 8.5px; font-weight: 700; line-height: 1.15; margin-top: 3px; }

  .storage { font-weight: 700; font-size: 14px; padding-bottom: 6px; border-bottom: 2px solid var(--paper); }
  .info-text { font-size: 10px; line-height: 1.35; margin: 8px 0 14px; }
  .info-text--web { font-weight: 700; }
</style>
</head>
<body>
<div class="artboard">
  <div class="sheet">
    <svg class="shapes" viewBox="0 0 1500 1100" width="1500" height="1100" aria-hidden="true">
      <defs>
        <linearGradient id="goldRing" x1="0" y1="0" x2="1" y2="1">
          <stop offset="0" stop-color="#d9ad45"/>
          <stop offset="0.6" stop-color="#dcb04a"/>
          <stop offset="1" stop-color="#a6822f"/>
        </linearGradient>
        <linearGradient id="goldBar" x1="0" y1="0" x2="0" y2="1">
          <stop offset="0" stop-color="#c59d3f"/>
          <stop offset="0.5" stop-color="#e2b84c"/>
          <stop offset="1" stop-color="#9c7a2c"/>
        </linearGradient>
      </defs>

      <!-- lid label -->
      <circle cx="750" cy="320" r="250" fill="url(#goldRing)"/>
      <circle cx="750" cy="320" r="212" fill="#ffffff"/>
      <circle cx="750" cy="320" r="207" fill="#050505"/>

      <!-- wrap label: front panel -->
      <polygon points="550,657 568,657 645,996 628,996" fill="url(#goldBar)"/>
      <polygon points="985,657 1003,657 927,996 910,996" fill="url(#goldBar)"/>
      <polygon points="580,657 975,657 898,996 655,996" fill="#050505"/>
      <line x1="685" y1="893" x2="868" y2="893" stroke="#3a3a3a" stroke-width="1"/>
      <rect x="742" y="916" width="70" height="80" fill="#b08a35"/>

      <!-- die cut outline -->
      <g fill="none" stroke="#d8262c" stroke-width="1.2">
        <path d="M118,770 Q775,640 1438,772"/>
        <path d="M172,1022 Q775,893 1383,1022"/>
        <path d="M118,770 L172,1022"/>
        <path d="M1438,772 L1383,1022"/>
      </g>
    </svg>

    <span class="brand-dot lid-dot"></span>
    <span class="brand-name lid-name">KESTREL RIDGE</span>
    <div class="olive-sprig" role="img" aria-label="Small white olive branch icon"></div>
    <div class="lid-tagline">Infused in olive oil</div>

    <span class="brand-dot front-dot"></span>
    <span class="brand-name front-name">KESTREL RIDGE</span>
    <div class="product-name">SHANKLISH</div>
    <div class="product-sub">Infused in olive oil</div>
    <div class="net-weight">200gm</div>

    <div class="side-panel side-panel--nutrition">
      <div class="nutrition-box">
        <div class="nutrition-title">Nutrition Facts</div>
        <div class="nutrition-meta">Serving per Package: 14<br>Serving size: 50g</div>
        <table class="nutrition-table">
          <tr><th></th><th>Quantity per serve</th><th>Quantity per 100g</th></tr>
          <tr><td>Energy:</td><td>720kJ</td><td>1440kJ</td></tr>
          <tr><td>Protein:</td><td>2.4g</td><td>4.8g</td></tr>
          <tr><td>Fat-total:</td><td>17.0g</td><td>34.0g</td></tr>
          <tr><td>-saturated:</td><td>2.5g</td><td>5.0g</td></tr>
          <tr><td>Carbohydrate:</td><td>2.9g</td><td>5.8g</td></tr>
          <tr><td>-sugars:</td><td>2.2g</td><td>4.4g</td></tr>
          <tr><td>Sodium:</td><td>155mg</td><td>310mg</td></tr>
        </table>
      </div>
      <div class="nutrition-origin">Made in Australia<br>from at least 99% Australian ingredients.</div>
    </div>

    <div class="side-panel side-panel--info">
      <div class="storage">Refrigerate below 4°</div>
      <p class="info-text">Contains milk, May contain traces of nuts.</p>
      <p class="info-text">Ingredients: Milk, A &amp; B probiotic cultures, Olive oil, Chilli &amp; Salt.</p>
      <p class="info-text">Made and Packed by Kestrel Ridge<br>18 Harbour Lane, Elmvale NSW 2199<br><span class="info-text--web">www.kestrelridgedairy.com.au</span></p>
    </div>
  </div>
</div>
</body>
</html>
```